Business Card for Health Food Store

I need a business card for a health food store that includes the following information.

=========
FRONT
=========

***White background***

Fernwick Provisions (logo)
Supplements - Health Foods - Remedies

2417 Larkwood Ave.
Alderbrook, CA 95012
(corner of Dunmore St.)

707-314-2296

FernwickProvisions.example
FernwickLiving@mailbox.example

On the right side of the front of the card, use a circle type seal with 25 large in the middle. Put the dates below it.
"Celebrating 25 Years"
1997 - 2022

*DO NOT USE A PERSON'S NAME ON THE CARD*

==========
BACK
==========

***Green background***

Full logo in white along with the social logos and handles.

FB Logo / FernwickProvisionsShop
IG Logo / FernwickProvisionsShop
Twitter Logo / VisitFernwick

When done I'll need the file in PSD and AI.

Target Market(s)

Surrounding local community

Industry/Entity Type

Retail Health Food Store

Contact Information for Business Card

See brief

Requirements
Must have
• Must be double-sided

```html
<!DOCTYPE html>
<html lang="en">
<head>
<meta charset="utf-8">
<title>Fernwick Provisions – Business Card</title>
<link rel="stylesheet" href="https://fonts.googleapis.com/css2?family=Nunito:wght@900&family=Oswald:wght@500;700&family=Roboto:wght@400;500&display=swap">
<style>
  :root {
    --leaf-green: #4caf32;
    --leaf-green-deep: #3f9a29;
    --ink: #2a2a2a;
    --paper: #fbfbf9;
    --stage: #e6ebe3;
    --white: #ffffff;
  }
  * { box-sizing: border-box; margin: 0; padding: 0; }
  html, body { width: 1200px; height: 900px; overflow: hidden; }
  body {
    background: var(--stage);
    display: flex;
    flex-direction: column;
    align-items: center;
    justify-content: center;
    gap: 44px;
    font-family: "Roboto", sans-serif;
  }
  .card {
    position: relative;
    width: 660px;
    height: 377px;
    border-radius: 26px;
    overflow: hidden;
    box-shadow: 0 10px 28px rgba(0,0,0,.14);
  }

  /* ---------- Front ---------- */
  .card--front { background: var(--paper); color: var(--ink); }
  .brand { position: absolute; left: 44px; top: 38px; }
  .brand__row { display: flex; align-items: center; gap: 12px; }
  .brand__dot {
    width: 28px; height: 28px; border-radius: 50%;
    background: var(--leaf-green);
  }
  .brand__name {
    font-family: "Nunito", sans-serif;
    font-weight: 900;
    font-size: 32px;
    line-height: 1;
    letter-spacing: -.5px;
  }
  .brand__tagline {
    margin-top: 6px;
    margin-left: 40px;
    font-family: "Oswald", sans-serif;
    font-weight: 500;
    font-size: 12px;
    letter-spacing: 1.2px;
    text-transform: uppercase;
    color: var(--leaf-green);
  }
  .contact {
    position: absolute; left: 44px; top: 130px;
    list-style: none;
    display: flex; flex-direction: column; gap: 14px;
  }
  .contact__item {
    display: flex; align-items: flex-start; gap: 12px;
    font-size: 15px; line-height: 1.3;
  }
  .contact__icon {
    flex: none;
    width: 22px; height: 22px; border-radius: 50%;
    background: var(--leaf-green);
    display: flex; align-items: center; justify-content: center;
  }
  .seal { position: absolute; right: 40px; bottom: 30px; width: 180px; height: 180px; }
  .seal text { font-family: "Oswald", sans-serif; font-weight: 700; }

  /* ---------- Back ---------- */
  .card--back { background: var(--leaf-green); color: var(--white); }
  .card__pattern {
    position: absolute; inset: 0;
    background: radial-gradient(circle at 50% 40%, #56b83b 0%, var(--leaf-green) 60%, var(--leaf-green-deep) 100%);
  }
  .back-brand {
    position: absolute; left: 0; right: 0; top: 96px;
    text-align: center;
  }
  .back-brand__row { display: inline-flex; align-items: center; gap: 14px; }
  .back-brand__dot { width: 36px; height: 36px; border-radius: 50%; border: 3px solid var(--white); }
  .back-brand__name {
    font-family: "Nunito", sans-serif; font-weight: 900;
    font-size: 46px; line-height: 1; letter-spacing: -.5px;
  }
  .back-brand__tagline {
    margin-top: 8px;
    font-family: "Oswald", sans-serif; font-weight: 500;
    font-size: 15px; letter-spacing: 1.6px; text-transform: uppercase;
  }
  .socials {
    position: absolute; left: 0; right: 0; bottom: 56px;
    list-style: none;
    display: flex; justify-content: center; gap: 30px;
  }
  .socials__item { display: flex; align-items: center; gap: 8px; font-size: 14px; }
  .socials__mark { width: 12px; height: 12px; border-radius: 50%; background: var(--white); }
</style>
</head>
<body>

  <section class="card card--front" aria-label="Business card front">
    <div class="brand">
      <div class="brand__row">
        <span class="brand__dot"></span>
        <span class="brand__name">Fernwick Provisions</span>
      </div>
      <p class="brand__tagline">Supplements · Health Foods · Remedies</p>
    </div>

    <ul class="contact">
      <li class="contact__item">
        <span class="contact__icon">
          <svg width="12" height="12" viewBox="0 0 12 12"><path d="M6 1a3.5 3.5 0 0 0-3.5 3.5C2.5 7.5 6 11 6 11s3.5-3.5 3.5-6.5A3.5 3.5 0 0 0 6 1z" fill="#fff"/><circle cx="6" cy="4.6" r="1.3" fill="#4caf32"/></svg>
        </span>
        <span>2417 Larkwood Ave.<br>Alderbrook, CA 95012</span>
      </li>
      <li class="contact__item">
        <span class="contact__icon">
          <svg width="12" height="12" viewBox="0 0 12 12"><path d="M3 1.5l1.6 2.3-.9 1.1a6 6 0 0 0 3.4 3.4l1.1-.9 2.3 1.6-.8 1.6C5.2 10.4 1.6 6.8 1.4 2.3z" fill="#fff"/></svg>
        </span>
        <span>707-314-2296</span>
      </li>
      <li class="contact__item">
        <span class="contact__icon">
          <svg width="12" height="12" viewBox="0 0 12 12"><rect x="1.5" y="3" width="9" height="6.5" rx="1" fill="none" stroke="#fff" stroke-width="1.2"/><path d="M1.8 3.4L6 6.6l4.2-3.2" fill="none" stroke="#fff" stroke-width="1.2"/></svg>
        </span>
        <span>FernwickLiving@mailbox.example</span>
      </li>
      <li class="contact__item">
        <span class="contact__icon">
          <svg width="12" height="12" viewBox="0 0 12 12"><circle cx="6" cy="6" r="4.5" fill="none" stroke="#fff" stroke-width="1.1"/><path d="M1.5 6h9M6 1.5c-2 2.5-2 6.5 0 9M6 1.5c2 2.5 2 6.5 0 9" fill="none" stroke="#fff" stroke-width="1"/></svg>
        </span>
        <span>FernwickProvisions.example</span>
      </li>
    </ul>

    <svg class="seal" viewBox="0 0 200 200" role="img" aria-label="Celebrating 25 years, 1997 to 2022">
      <defs>
        <path id="seal-top" d="M30 100 A70 70 0 0 1 170 100"/>
        <path id="seal-bottom" d="M26 100 A74 74 0 0 0 174 100"/>
      </defs>
      <circle cx="100" cy="100" r="96" fill="none" stroke="var(--leaf-green)" stroke-width="6"/>
      <circle cx="100" cy="100" r="88" fill="none" stroke="var(--leaf-green)" stroke-width="1.5"/>
      <text font-size="19" fill="var(--leaf-green)" letter-spacing="2"><textPath href="#seal-top" startOffset="50%" text-anchor="middle">CELEBRATING</textPath></text>
      <text font-size="19" fill="var(--leaf-green)" letter-spacing="2"><textPath href="#seal-bottom" startOffset="50%" text-anchor="middle">1997 · 2022</textPath></text>
      <circle cx="100" cy="100" r="52" fill="var(--leaf-green)"/>
      <circle cx="100" cy="100" r="46" fill="none" stroke="#fff" stroke-width="1.5"/>
      <text x="100" y="108" text-anchor="middle" font-size="44" fill="#fff">25</text>
      <text x="100" y="130" text-anchor="middle" font-size="15" fill="#fff" letter-spacing="2">YEARS</text>
      <circle cx="26" cy="100" r="3" fill="var(--leaf-green)"/>
      <circle cx="174" cy="100" r="3" fill="var(--leaf-green)"/>
    </svg>
  </section>

  <section class="card card--back" aria-label="Business card back">
    <div class="card__pattern" role="img" aria-label="Faint repeating leaf pattern on green"></div>
    <div class="back-brand">
      <div class="back-brand__row">
        <span class="back-brand__dot"></span>
        <span class="back-brand__name">Fernwick Provisions</span>
      </div>
      <p class="back-brand__tagline">Supplements · Health Foods · Remedies</p>
    </div>
    <ul class="socials">
      <li class="socials__item"><span class="socials__mark"></span>FernwickProvisionsShop</li>
      <li class="socials__item"><span class="socials__mark"></span>FernwickProvisionsShop</li>
      <li class="socials__item"><span class="socials__mark"></span>VisitFernwick</li>
    </ul>
  </section>

</body>
</html>
```